Board Presentation template

Design a simple and clean PowerPoint slide templates for a Board meeting. The slides should have predominantly white backgrounds and use the colors of our Logo (attached): Tones of grey and orange and blue.
The company name is called Harrowgate Loadline Works.
It sell, calibrate, service and repair industrial and commercial scales of all types. In particular, Truck scales, floor scales, counting scales and benchtop scales.
There is no website for Harrowgate Loadline Works, but we have three affiliates that have their own websites:
https://www.quillbeamweigh.com/
https://northvanetruckandbalancegroup.com/
https://kbtare.com/
Target Market(s)
Industrial and Commercial Weighing systems
Industry/Entity Type
Look and feel
Each slider illustrates characteristics of the customer's brand and the style your logo design should communicate.

```html
<!DOCTYPE html>
<html lang="en">
<head>
<meta charset="utf-8">
<title>Harrowgate Loadline Works — Board Deck 2025 Template</title>
<link href="https://fonts.googleapis.com/css2?family=Oswald:wght@500;600&family=Poppins:wght@400;500;600&family=Inter:wght@400;500&display=swap" rel="stylesheet">
<style>
:root{
  --red:#d13a2c;
  --red-dark:#7a1510;
  --navy:#1f4e79;
  --blue:#2f5f8a;
  --steel:#8aa5bf;
  --steel-light:#c6d4e1;
  --ink:#1e2329;
  --grey:#4a5560;
  --grey-mid:#8a939b;
  --grey-light:#e4e8ec;
  --slate:#3b444c;
  --canvas:#cfcfd0;
  --ui-dark:#2b2b2b;
  --ui-mid:#3a3a3a;
  --ui-text:#e6e6e6;
}
*{margin:0;padding:0;box-sizing:border-box}
html,body{width:1200px;height:1162px;overflow:hidden;background:var(--canvas)}
body{position:relative;font-family:"Poppins",sans-serif;color:var(--ink)}
.abs{position:absolute}
.cond{font-family:"Oswald",sans-serif;font-weight:600;text-transform:uppercase;letter-spacing:-.2px}

/* ---------- editor window ---------- */
.editor{left:0;top:29px;width:570px;height:425px;background:#262626}
.ribbon{left:0;top:0;width:570px;height:69px;background:var(--ui-dark);border-bottom:1px solid #444}
.menu{left:5px;top:5px;font-family:"Inter",sans-serif;font-size:7px;color:var(--ui-text);display:flex;gap:13px}
.ui-btn{top:4px;height:13px;border:1px solid #666;border-radius:3px;font-family:"Inter",sans-serif;font-size:6.5px;color:var(--ui-text);display:flex;align-items:center;justify-content:center;gap:3px}
.ui-btn.share{background:#e0702a;border-color:#e0702a}
.tool{background:#555;border-radius:1px}
.tool-label{font-family:"Inter",sans-serif;font-size:5.5px;color:var(--ui-text);text-align:center;line-height:1.15}
.editor-slide{left:206px;top:69px;width:325px;height:343px;background:#fff;overflow:hidden}
.big-title{font-family:"Oswald",sans-serif;font-weight:600;font-size:50px;line-height:1;letter-spacing:-1px}
.selection{border:1px solid #9a9a9a}
.handle{width:4px;height:4px;background:#fff;border:1px solid #888}

.pane{left:35px;top:155px;width:171px;height:386px;background:var(--ui-dark)}
.pane-tabs{left:3px;top:5px;display:flex;gap:11px;font-family:"Inter",sans-serif;font-size:7px;color:var(--ui-text)}
.pane-tabs span:first-child{font-weight:500;border-bottom:1px solid #fff}
.pane-tools{font-family:"Inter",sans-serif;font-size:5.5px;color:var(--ui-text)}
.slide-no{font-family:"Inter",sans-serif;font-size:6.5px;color:var(--ui-text)}
.mini{width:129px;height:73px;background:#fff;overflow:hidden}
.mini.sel{outline:2px solid var(--red)}

.dropdown{left:372px;top:64px;width:105px;height:219px;background:#242424;border:1px solid #555;border-radius:3px;font-family:"Inter",sans-serif;font-size:7px;color:var(--ui-text)}
.dropdown .lbl{position:absolute;left:4px}
.nofill{left:4px;top:16px;width:95px;height:11px;border:1px solid var(--red);text-align:center;font-size:6.5px;line-height:9px}
.sw-row{left:4px;display:flex;gap:1px}
.sw-row i{display:block;width:8.6px;height:7px}
.shade-grid{left:4px;top:57px;display:flex;gap:1px}
.shade-grid i{display:block;width:8.6px;height:43px}
.dd-sep{left:0;top:161px;width:103px;height:1px;background:#444}
.dd-item{left:4px;display:flex;align-items:center;gap:4px}
.dd-item b{display:inline-block;width:8px;height:7px;border:1px solid #aaa;background:#666}

/* ---------- callouts ---------- */
.callout{background:var(--red);color:#fff;font-family:"Oswald",sans-serif;font-weight:500;display:flex;align-items:center;justify-content:center}

/* ---------- large slides ---------- */
.slide{background:#fff;overflow:hidden}
.seeing-title{font-size:9.5px;font-weight:600;color:#7f9bb5}
.seeing-body{font-size:6.2px;line-height:1.7;color:#333}
.placeholder{border:1.5px dashed #9aa;border-top:none}
.insert-btn{border:1px solid #bbb;border-radius:2px;font-family:"Inter",sans-serif;font-size:9px;display:flex;align-items:center;gap:5px;justify-content:center;background:#fff}
.brand{font-family:"Oswald",sans-serif;font-weight:500;color:var(--grey);text-transform:uppercase;line-height:1;display:flex;align-items:center;gap:3px}
.brand i{display:block;border-radius:50%;border:1px solid var(--grey)}
/* stacked mark for cover slides: circle above a two-line name */
.brand-stack{font-family:"Oswald",sans-serif;font-weight:500;color:var(--grey);text-transform:uppercase;line-height:1.1;display:flex;flex-direction:column;align-items:center;text-align:center;gap:2px}
.brand-stack i{display:block;border-radius:50%;border:1px solid var(--grey)}
.brand-stack.light{color:#fff}
.brand-stack.light i{border-color:#fff}
.quote-line{left:0;width:567px;text-align:center;font-size:21.5px;line-height:1.2;color:var(--ink)}
.quote-line em{font-style:normal;font-weight:600;color:var(--red)}

/* ---------- thumbnail grid ---------- */
.t{position:absolute;width:169px;height:95px;background:#fff;overflow:hidden}
.tt{position:absolute;left:9px;top:9px;font-family:"Oswald",sans-serif;font-weight:600;font-size:9px;line-height:1;text-transform:uppercase;color:var(--ink);letter-spacing:-.2px}
.tm{position:absolute;right:5px;top:4px;font-family:"Oswald",sans-serif;font-weight:500;font-size:3px;color:var(--grey);text-transform:uppercase;display:flex;align-items:center;gap:1px}
.tm i{display:block;width:3px;height:3px;border-radius:50%;border:.5px solid var(--grey)}
.tiny{position:absolute;font-size:2.6px;line-height:1.35;color:#777}
.num{position:absolute;font-family:"Oswald",sans-serif;font-weight:600;line-height:1}
</style>
</head>
<body>

<!-- ===== Editor window ===== -->
<section class="abs editor">
  <div class="abs ribbon">
    <div class="abs menu"><span>Record</span><span>Review</span><span>View</span><span>PDF Tools</span><span>Shape Format</span></div>
    <div class="abs ui-btn" style="left:409px;width:44px">● Record</div>
    <div class="abs ui-btn" style="left:458px;width:55px">▭ Comments</div>
    <div class="abs ui-btn share" style="left:519px;width:47px">⇪ Share ⌄</div>
    <div class="abs tool" style="left:4px;top:28px;width:10px;height:8px"></div>
    <div class="abs tool" style="left:36px;top:28px;width:10px;height:8px"></div>
    <div class="abs tool" style="left:60px;top:28px;width:14px;height:8px"></div>
    <div class="abs tool" style="left:80px;top:28px;width:14px;height:8px"></div>
    <div class="abs tool" style="left:109px;top:28px;width:14px;height:8px"></div>
    <div class="abs tool" style="left:141px;top:28px;width:12px;height:8px"></div>
    <div class="abs tool" style="left:175px;top:28px;width:12px;height:8px"></div>
    <div class="abs tool" style="left:195px;top:24px;width:16px;height:12px;background:#3f7d4a"></div>
    <div class="abs tool" style="left:236px;top:24px;width:14px;height:12px;background:#3f6f9e"></div>
    <div class="abs tool" style="left:262px;top:24px;width:14px;height:12px;background:#3f6f9e"></div>
    <div class="abs tool" style="left:288px;top:24px;width:14px;height:12px;border:1px solid #5a8fd0;background:none"></div>
    <div class="abs tool" style="left:319px;top:22px;width:14px;height:14px;background:#e0a03a"></div>
    <div class="abs tool" style="left:346px;top:22px;width:16px;height:16px;background:none;border:1px solid #888"></div>
    <div class="abs tool-label" style="left:342px;top:40px">Quick<br>Styles</div>
    <div class="abs tool-label" style="left:376px;top:25px;color:#fff">◩ Shape Fill ⌄</div>
    <div class="abs tool" style="left:445px;top:22px;width:14px;height:14px;background:none;border:1px solid var(--red)"></div>
    <div class="abs tool" style="left:480px;top:22px;width:16px;height:14px;background:none;border:1px solid #aaa"></div>
    <div class="abs tool-label" style="left:476px;top:42px">Designer</div>
    <div class="abs tool" style="left:527px;top:22px;width:14px;height:14px;background:none;border:1px solid #5a8fd0"></div>
    <div class="abs tool-label" style="left:512px;top:40px">Create PDF<br>and share link</div>
  </div>

  <div class="abs editor-slide">
    <div class="abs big-title" style="left:-8px;top:119px;color:var(--red)">BOARD</div>
    <div class="abs big-title" style="left:-8px;top:162px;color:var(--slate)">DECK 2025</div>
    <div class="abs selection" style="left:0;top:122px;width:237px;height:97px"></div>
    <div class="abs handle" style="left:106px;top:120px"></div>
    <div class="abs handle" style="left:106px;top:217px"></div>
    <div class="abs handle" style="left:235px;top:217px"></div>
    <div class="abs" style="left:107px;top:108px;width:6px;height:6px;border:1px solid #888;border-radius:50%"></div>
  </div>
</section>

<!-- slide pane -->
<section class="abs pane">
  <div class="abs pane-tabs"><span>Home</span><span>Insert</span><span>Draw</span><span>Design</span><span>Transitions</span></div>
  <div class="abs pane-tools" style="left:4px;top:22px;width:14px;height:14px;background:#7a6a3a;border-radius:1px"></div>
  <div class="abs pane-tools" style="left:6px;top:41px">Paste</div>
  <div class="abs pane-tools" style="left:36px;top:23px;line-height:2">✂ Cut<br>⎘ Copy ⌄<br>✎ Format</div>
  <div class="abs pane-tools" style="left:78px;top:22px;width:14px;height:12px;border:1px solid #aaa"></div>
  <div class="abs pane-tools" style="left:80px;top:39px;text-align:center;line-height:1.1">New<br>Slide</div>
  <div class="abs pane-tools" style="left:106px;top:23px;line-height:2">▤ Layout ⌄<br>▤ Reset<br>▤ Section ⌄</div>
  <div class="abs" style="left:165px;top:120px;width:4px;height:60px;background:#555;border-radius:2px"></div>

  <div class="abs slide-no" style="left:5px;top:63px">1</div>
  <div class="abs mini sel" style="left:14px;top:62px">
    <div class="abs brand-stack" style="left:24px;top:26px;width:30px;font-size:3px"><i style="width:6px;height:6px"></i>Harrowgate<br>Loadline Works</div>
    <div class="abs cond" style="left:57px;top:26px;font-size:9.5px;line-height:.95;color:var(--red)">Board<br><span style="color:var(--slate)">Deck 2025</span></div>
  </div>
  <div class="abs slide-no" style="left:5px;top:145px">2</div>
  <div class="abs mini" style="left:14px;top:145px;background:var(--red)">
    <div class="abs brand-stack light" style="left:15px;top:26px;width:30px;font-size:3px"><i style="width:6px;height:6px"></i>Harrowgate<br>Loadline Works</div>
    <div class="abs cond" style="left:50px;top:25px;font-size:9.5px;line-height:.95;color:#fff">Boardmeeting<br>Deck 2025</div>
  </div>
  <div class="abs slide-no" style="left:5px;top:227px">3</div>
  <div class="abs mini" style="left:14px;top:227px">
    <div class="abs" style="left:58px;top:17px;width:12px;height:12px;border-radius:50%;background:var(--red);color:#fff;font-size:6px;text-align:center;line-height:12px;font-weight:600">”</div>
    <div class="abs" style="left:0;top:31px;width:129px;text-align:center;font-size:3.6px;font-weight:600">– Name, CEO</div>
    <div class="abs" style="left:0;top:40px;width:129px;text-align:center;font-size:4.2px;line-height:1.3"><b style="color:var(--red);font-weight:600">Now there is a way to people who<br>already</b> looking something, you offer<br>Our relevance</div>
    <div class="abs" style="left:8px;top:63px;width:113px;height:2px;background:var(--steel)"></div>
  </div>
  <div class="abs slide-no" style="left:5px;top:309px">4</div>
  <div class="abs mini" style="left:14px;top:309px">
    <div class="abs cond" style="left:7px;top:6px;font-size:6px">Agenda</div>
    <svg class="abs" style="left:7px;top:14px" width="30" height="20"><path d="M1 1 L16 16 L28 16" stroke="var(--steel)" stroke-width=".6" fill="none"/></svg>
    <div class="abs" style="left:53px;top:7px;font-size:3.8px;line-height:1.6;font-weight:500">1 CEO Update<br>2 Highlight<br>3 User Growth<br>4 Product Roadmap<br>5 Statement<br>6 Team Update<br>7 Get in touch</div>
    <div class="abs brand" style="left:5px;top:62px;font-size:2.6px"><i style="width:4px;height:4px"></i>Harrowgate Loadline Works</div>
  </div>
</section>

<!-- colour dropdown -->
<section class="abs dropdown">
  <div class="lbl" style="top:5px;color:#777">▢ High Contrast Only</div>
  <div class="abs nofill">No Fill</div>
  <div class="lbl" style="top:33px">Theme Colours</div>
  <div class="abs sw-row" style="top:46px">
    <i style="background:#fff"></i><i style="background:#000"></i><i style="background:var(--red)"></i><i style="background:#1f3a55"></i><i style="background:var(--blue)"></i><i style="background:#5b87ad"></i><i style="background:#8fb0cc"></i><i style="background:#7a8590"></i><i style="background:#c9d1d8"></i><i style="background:#6d94b8"></i>
  </div>
  <div class="abs shade-grid">
    <i style="background:linear-gradient(#f2f2f2 20%,#d9d9d9 20% 40%,#bfbfbf 40% 60%,#a5a5a5 60% 80%,#7f7f7f 80%)"></i>
    <i style="background:linear-gradient(#7f7f7f 20%,#595959 20% 40%,#404040 40% 60%,#262626 60% 80%,#0d0d0d 80%)"></i>
    <i style="background:linear-gradient(#f6d5d1 20%,#ecaba3 20% 40%,#e38076 40% 60%,#a12b20 60% 80%,#6b1d15 80%)"></i>
    <i style="background:linear-gradient(#c9d7e5 20%,#93afcb 20% 40%,#5d87b1 40% 60%,#172c40 60% 80%,#0f1d2b 80%)"></i>
    <i style="background:linear-gradient(#d1e0ee 20%,#a3c1dd 20% 40%,#75a2cc 40% 60%,#234768 60% 80%,#172f45 80%)"></i>
    <i style="background:linear-gradient(#dee7ef 20%,#bdcfdf 20% 40%,#9cb7cf 40% 60%,#416689 60% 80%,#2b445b 80%)"></i>
    <i style="background:linear-gradient(#e9eff5 20%,#d2dfeb 20% 40%,#bccfe0 40% 60%,#5883aa 60% 80%,#375873 80%)"></i>
    <i style="background:linear-gradient(#e4e6e9 20%,#cacdd2 20% 40%,#afb5bc 40% 60%,#5b636b 60% 80%,#3d4247 80%)"></i>
    <i style="background:linear-gradient(#f4f6f7 20%,#e9edef 20% 40%,#dee3e7 40% 60%,#8e9cab 60% 80%,#5a6774 80%)"></i>
    <i style="background:linear-gradient(#e1e9f1 20%,#c4d4e3 20% 40%,#a6bfd5 40% 60%,#4a729a 60% 80%,#314c67 80%)"></i>
  </div>
  <div class="lbl" style="top:107px">Standard Colours</div>
  <div class="abs sw-row" style="top:118px">
    <i style="background:#c00000"></i><i style="background:#ff0000"></i><i style="background:#ffc000"></i><i style="background:#ffff00"></i><i style="background:#92d050"></i><i style="background:#00b050"></i><i style="background:#00b0f0"></i><i style="background:#0070c0"></i><i style="background:#002060"></i><i style="background:#7030a0"></i>
  </div>
  <div class="lbl" style="top:135px">Recent Colours</div>
  <div class="abs sw-row" style="top:147px">
    <i style="background:#b5483a"></i><i style="background:var(--blue)"></i><i style="background:var(--red)"></i><i style="background:#555d66"></i><i style="background:#fff"></i>
  </div>
  <div class="abs dd-sep"></div>
  <div class="abs dd-item" style="top:167px"><b></b>More Fill Colours...</div>
  <div class="abs dd-item" style="top:180px"><b></b>Picture...</div>
  <div class="abs dd-item" style="top:193px"><b></b>Gradient<span style="position:absolute;left:90px">▶</span></div>
  <div class="abs dd-item" style="top:206px"><b></b>Texture<span style="position:absolute;left:90px">▶</span></div>
</section>

<div class="abs callout" style="left:35px;top:66px;width:306px;height:67px;font-size:22px">Brand colour pallet loaded</div>

<!-- ===== What am I seeing slide ===== -->
<section class="abs slide" style="left:600px;top:0;width:567px;height:167px">
  <div class="abs seeing-title" style="left:31px;top:16px">What am I Seeing</div>
  <div class="abs" style="left:31px;top:31px;width:155px;height:1px;background:#dde3e8"></div>
  <p class="abs seeing-body" style="left:31px;top:37px;width:160px">We are an award-winning creative agency with an elite team and years of experience. With attention to detail and rigorous brainstorming We are an award-winning creative agency</p>
  <div class="abs num" style="left:30px;top:93px;font-size:38px;color:var(--ink)">2M</div>
  <div class="abs" style="left:31px;top:131px;font-size:5.5px">Products</div>
  <svg class="abs" style="left:89px;top:98px" width="30" height="30"><path d="M15 2 V28 M2 15 H28" stroke="#d9dde1" stroke-width="4"/></svg>
  <svg class="abs" style="left:134px;top:92px" width="40" height="32"><path d="M3 17 L14 28 L37 3" stroke="var(--red)" stroke-width="5" fill="none"/></svg>
  <div class="abs placeholder" style="left:237px;top:0;width:298px;height:129px"></div>
  <div class="abs insert-btn" style="left:343px;top:31px;width:88px;height:19px"><span style="display:inline-block;width:9px;height:8px;border:1px solid #557"></span>Insert Picture</div>
</section>

<!-- ===== Quote slide ===== -->
<section class="abs slide" style="left:600px;top:189px;width:567px;height:319px">
  <div class="abs brand" style="left:474px;top:16px;font-size:8px;width:80px;line-height:1.1"><i style="width:9px;height:9px;flex:none"></i>Harrowgate Loadline Works</div>
  <div class="abs" style="left:252px;top:70px;width:62px;height:62px;border-radius:50%;background:#f3f3f3;box-shadow:0 1px 3px rgba(0,0,0,.15)"></div>
  <div class="abs" style="left:260px;top:78px;width:46px;height:46px;border-radius:50%;background:var(--red);color:#fff;font-size:28px;font-weight:600;text-align:center;line-height:56px">”</div>
  <div class="abs" style="left:0;top:138px;width:567px;text-align:center;font-size:16px;font-weight:600">– Name, CEO</div>
  <div class="abs quote-line" style="top:180px"><em>Now there is a way to people who</em></div>
  <div class="abs quote-line" style="top:206px"><em>already</em> looking something, you offer</div>
  <div class="abs quote-line" style="top:232px">Our relevance</div>
  <div class="abs" style="left:32px;top:277px;width:503px;height:10px;background:var(--steel)"></div>
</section>

<div class="abs callout" style="left:834px;top:156px;width:221px;height:66px;font-size:21px">Image Place Holders</div>
<svg class="abs" style="left:930px;top:141px" width="22" height="16"><path d="M0 16 L11 0 L22 16Z" fill="var(--red)"/></svg>
<div class="abs callout" style="left:466px;top:364px;width:185px;height:68px;font-size:21px">Editable Text</div>
<svg class="abs" style="left:650px;top:384px" width="16" height="28"><path d="M0 0 L16 14 L0 28Z" fill="var(--red)"/></svg>

<!-- ===== Thumbnail grid: row 1 ===== -->
<div class="t" style="left:33px;top:559px">
  <div class="abs brand-stack" style="left:27px;top:32px;width:38px;font-size:3.8px"><i style="width:9px;height:9px"></i>Harrowgate<br>Loadline Works</div>
  <div class="abs cond" style="left:74px;top:33px;font-size:12.5px;line-height:.95;color:var(--red)">Board<br><span style="color:var(--slate)">Deck 2025</span></div>
</div>
<div class="t" style="left:226px;top:559px;background:var(--red)">
  <div class="abs brand-stack light" style="left:21px;top:32px;width:38px;font-size:3.8px"><i style="width:9px;height:9px"></i>Harrowgate<br>Loadline Works</div>
  <div class="abs cond" style="left:65px;top:33px;font-size:12.5px;line-height:.95;color:#fff">Boardmeeting<br>Deck 2025</div>
</div>
<div class="t" style="left:419px;top:559px">
  <div class="tm"><i></i>Harrowgate Loadline Works</div>
  <div class="abs" style="left:77px;top:22px;width:15px;height:15px;border-radius:50%;background:var(--red);color:#fff;font-size:8px;text-align:center;line-height:18px;font-weight:600">”</div>
  <div class="abs" style="left:0;top:41px;width:169px;text-align:center;font-size:4.6px;font-weight:600">– Name, CEO</div>
  <div class="abs" style="left:0;top:52px;width:169px;text-align:center;font-size:5.6px;line-height:1.3"><b style="color:var(--red);font-weight:600">Now there is a way to people who<br>already</b> looking something, you offer<br>Our relevance</div>
  <div class="abs" style="left:10px;top:83px;width:149px;height:3px;background:var(--steel)"></div>
</div>
<div class="t" style="left:612px;top:559px">
  <div class="tm"><i></i>Harrowgate Loadline Works</div>
  <div class="tt">Agenda</div>
  <svg class="abs" style="left:10px;top:20px" width="60" height="30"><path d="M1 1 L34 26 L58 26" stroke="var(--steel)" stroke-width=".6" fill="none"/></svg>
  <div class="abs" style="left:70px;top:10px;font-size:5px;line-height:1.6;font-weight:500">1 CEO Update<br>2 Highlight<br>3 User Growth<br>4 Product Roadmap<br>5 Statement<br>6 Team Update<br>7 Get in touch</div>
  <div class="abs brand" style="left:7px;top:78px;font-size:3px"><i style="width:5px;height:5px"></i>Harrowgate Loadline Works</div>
</div>
<div class="t" style="left:805px;top:559px">
  <div class="tm"><i></i>Harrowgate Loadline Works</div>
  <div class="tt">Big Picture</div>
  <svg class="abs" style="left:8px;top:48px" width="155" height="5"><g stroke="#bbb" stroke-width=".5"><path d="M0 3 H25 M38 3 H63 M77 3 H102 M116 3 H141"/></g></svg>
  <div class="abs" style="left:8px;top:42px;width:155px;display:flex;gap:25px;font-size:3.2px;font-weight:600"><span>01</span><span style="margin-left:4px">02</span><span style="margin-left:4px">03</span><span style="margin-left:4px">04</span></div>
  <div class="abs" style="left:8px;top:61px;width:155px;display:flex;gap:14px;font-size:2.6px;color:var(--red);font-weight:600"><span style="width:25px">CEO Updates</span><span style="width:25px">Highlight</span><span style="width:25px">Lowlight</span><span style="width:25px">Current Priority</span></div>
  <div class="abs" style="left:8px;top:66px;width:155px;display:flex;gap:14px;font-size:2.3px;color:#888;line-height:1.3"><span style="width:25px">Short note on this area here</span><span style="width:25px">Short note on this area here</span><span style="width:25px">Short note on this area here</span><span style="width:25px">Short note on this area here</span></div>
</div>
<div class="t" style="left:998px;top:559px;background:linear-gradient(115deg,#a32a20,#4a0f0b 55%,#1a0807)" role="img" aria-label="Dark red title background with freight photo area">
  <div class="tm" style="color:#fff"><i style="border-color:#fff"></i>Harrowgate Loadline Works</div>
  <div class="abs" style="left:9px;top:41px;font-size:8.6px;font-weight:600;color:#fff;line-height:1.15">Freight Visibility<br>Made Simple</div>
  <div class="tiny" style="left:9px;top:84px;color:#ddd">Continue to next slide</div>
</div>

<!-- row 2 -->
<div class="t" style="left:33px;top:678px">
  <div class="tm"><i></i>Harrowgate Loadline Works</div>
  <div class="tt">CEO Update</div>
  <svg class="abs" style="left:0;top:0" width="169" height="95"><g stroke="#bbb" stroke-width=".6" fill="none"><path d="M37 64 L84 37 L133 64 M37 64 H133"/></g>
  <g fill="#fff" stroke="var(--grey-mid)" stroke-width="1.2"><circle cx="84" cy="37" r="6"/><circle cx="37" cy="64" r="6"/><circle cx="133" cy="64" r="6"/></g>
  <circle cx="84" cy="64" r="9" fill="#fff" stroke="var(--slate)" stroke-width="2"/><path d="M80 64 L83 67 L89 60" stroke="var(--red)" stroke-width="1.5" fill="none"/>
  <g font-size="3" font-family="Poppins" text-anchor="middle" fill="#333"><text x="84" y="39">02</text><text x="37" y="66">01</text><text x="133" y="66">03</text></g>
  <g font-size="2.6" font-family="Poppins" font-weight="600" text-anchor="middle" fill="#222"><text x="84" y="26">The Second Topic</text><text x="28" y="52">The First Topic</text><text x="141" y="52">The Third Topic</text><text x="84" y="85">BOARD OPTIMIZE</text></g></svg>
</div>
<div class="t" style="left:226px;top:678px">
  <div class="tm"><i></i>Harrowgate Loadline Works</div>
  <div class="abs brand-stack" style="left:6px;top:8px;width:26px;font-size:2.8px"><i style="width:7px;height:7px"></i>Harrowgate<br>Loadline Works</div>
  <div class="abs cond" style="left:9px;top:70px;font-size:8.5px;line-height:.95">Hard to create<br>Portfolio</div>
  <div class="abs" style="left:74px;top:19px;width:89px;height:70px;background:#f7f8f9"></div>
  <div class="num" style="left:78px;top:21px;font-size:10.5px">7,22+</div>
  <div class="num" style="left:125px;top:21px;font-size:10.5px">9,57K</div>
  <div class="num" style="left:78px;top:58px;font-size:10.5px;color:var(--red)">4,22M</div>
  <div class="num" style="left:125px;top:58px;font-size:10.5px">6,37%</div>
  <div class="tiny" style="left:78px;top:35px;width:38px">Short note on this figure</div>
  <div class="tiny" style="left:125px;top:35px;width:38px">Short note on this figure</div>
  <div class="tiny" style="left:78px;top:72px;width:38px">Short note on this figure</div>
  <div class="tiny" style="left:125px;top:72px;width:38px">Short note on this figure</div>
</div>
<div class="t" style="left:419px;top:678px">
  <div class="tm"><i></i>Harrowgate Loadline Works</div>
  <div class="tt">Current Priorities</div>
  <svg class="abs" style="left:0;top:0" width="169" height="95"><circle cx="72" cy="53" r="15" fill="var(--steel)" opacity=".8"/><circle cx="57" cy="72" r="9" fill="#9aa0a6"/><circle cx="43" cy="50" r="19" fill="var(--red)"/>
  <g font-family="Oswald" font-weight="600" fill="#fff" text-anchor="middle"><text x="43" y="52" font-size="10">29K</text><text x="74" y="55" font-size="6" fill="#1e2329">80%</text><text x="57" y="75" font-size="5" fill="#1e2329">20%</text></g></svg>
  <div class="abs" style="left:103px;top:52px;width:57px;height:13px;background:#eef2f6"></div>
  <div class="tiny" style="left:118px;top:32px;width:42px"><b style="color:#222">M. Objectives</b><br>Short line of text here now</div>
  <div class="tiny" style="left:118px;top:53px;width:42px"><b style="color:#222">M. Objectives</b><br>Short line of text here now</div>
  <div class="tiny" style="left:118px;top:74px;width:42px"><b style="color:#222">M. Tactics</b><br>Short line of text here now</div>
</div>
<div class="t" style="left:612px;top:678px">
  <div class="tm"><i></i>Harrowgate Loadline Works</div>
  <div class="tt">Funding Usage Plan</div>
  <div class="tiny" style="left:9px;top:46px;width:55px"><b style="color:#222">Subtitle here</b><br>Short paragraph about the funding plan and where it goes this year.</div>
  <div class="num" style="left:9px;top:74px;font-size:10px">2M</div>
  <div class="num" style="left:45px;top:74px;font-size:10px;color:var(--blue)">45%</div>
  <svg class="abs" style="left:100px;top:20px" width="66" height="70"><g><rect x="4" y="38" width="5" height="26" fill="var(--navy)"/><rect x="20" y="4" width="5" height="60" fill="var(--steel)"/><rect x="36" y="24" width="5" height="40" fill="var(--steel-light)"/><rect x="52" y="40" width="5" height="24" fill="#d9dbf5"/></g></svg>
</div>
<div class="t" style="left:805px;top:678px;background:linear-gradient(120deg,#0f1b26,#1c3a55 60%,#2a5f8a)" role="img" aria-label="Dark blue features background with picture area">
  <div class="tm" style="color:#fff"><i style="border-color:#fff"></i>Harrowgate Loadline Works</div>
  <div class="abs cond" style="left:4px;top:27px;font-size:46px;color:#0a0e12;letter-spacing:-1px">Features</div>
  <div class="abs" style="left:34px;top:19px;width:101px;height:63px;border:.6px solid #9ab"></div>
  <div class="abs" style="left:72px;top:48px;width:24px;height:5px;background:#fff;font-size:2.5px;text-align:center;line-height:5px">Insert Picture</div>
</div>
<div class="t" style="left:998px;top:678px">
  <div class="tm"><i></i>Harrowgate Loadline Works</div>
  <div class="tt">Lowlight</div>
  <svg class="abs" style="left:8px;top:26px" width="50" height="60"><rect x="2" y="4" width="3" height="56" fill="var(--navy)"/><rect x="9" y="14" width="3" height="46" fill="var(--steel)"/><rect x="16" y="30" width="3" height="30" fill="#9aa0a6"/><rect x="23" y="22" width="3" height="38" fill="var(--steel)"/><rect x="30" y="40" width="3" height="20" fill="#9aa0a6"/><rect x="37" y="26" width="3" height="34" fill="var(--steel-light)"/></svg>
  <div class="tiny" style="left:67px;top:37px;width:28px;color:#222"><b>Good idea</b> makes everything better</div>
  <div class="num" style="left:67px;top:52px;font-size:9px;color:var(--blue)">2.10B</div>
  <div class="num" style="left:67px;top:70px;font-size:9px;color:var(--steel)">1.09M</div>
  <svg class="abs" style="left:118px;top:37px" width="10" height="50"><circle cx="5" cy="4" r="3.5" fill="var(--steel)"/><circle cx="5" cy="23" r="3.5" fill="var(--blue)"/><circle cx="5" cy="42" r="3.5" fill="var(--steel-light)"/></svg>
  <div class="tiny" style="left:131px;top:36px;width:33px"><b style="color:#222">Subtitle here</b><br>Short note line</div>
  <div class="tiny" style="left:131px;top:55px;width:33px"><b style="color:#222">Subtitle here</b><br>Short note line</div>
  <div class="tiny" style="left:131px;top:74px;width:33px"><b style="color:#222">Subtitle here</b><br>Short note line</div>
</div>

<!-- row 3 -->
<div class="t" style="left:33px;top:797px">
  <div class="tm"><i></i>Harrowgate Loadline Works</div>
  <div class="tt">Highlight</div>
  <svg class="abs" style="left:0;top:0" width="169" height="95"><path d="M19 52 H145" stroke="#ddd" stroke-width=".6"/><circle cx="19" cy="52" r="6" fill="var(--blue)"/><circle cx="61" cy="52" r="6" fill="var(--steel)"/><circle cx="103" cy="52" r="6" fill="var(--steel-light)"/><circle cx="145" cy="52" r="6" fill="var(--navy)"/></svg>
  <div class="abs" style="left:9px;top:73px;width:155px;display:flex;gap:11px;font-size:2.6px;line-height:1.35;color:#777"><span style="width:31px"><b style="color:#222">Team</b><br>Short note on this point</span><span style="width:31px"><b style="color:#222">Product</b><br>Short note on this point</span><span style="width:31px"><b style="color:#222">Company</b><br>Short note on this point</span><span style="width:31px"><b style="color:#222">Highlight</b><br>Short note on this point</span></div>
</div>
<div class="t" style="left:226px;top:797px">
  <div class="tm"><i></i>Harrowgate Loadline Works</div>
  <div class="tt">Funding Usage<br>Plan</div>
  <div class="num" style="left:15px;top:57px;font-size:8px">$1.3<small style="font-size:3px">Billion</small></div>
  <div class="num" style="left:50px;top:57px;font-size:8px">$200<small style="font-size:3px">Billion</small></div>
  <div class="num" style="left:15px;top:76px;font-size:8px">$5.2<small style="font-size:3px">Million</small></div>
  <div class="num" style="left:50px;top:76px;font-size:8px">$23<small style="font-size:3px">Million</small></div>
  <svg class="abs" style="left:94px;top:12px" width="70" height="78" viewBox="0 0 70 78"><circle cx="35" cy="39" r="28" fill="none" stroke="#dde4eb" stroke-width="10"/><circle cx="35" cy="39" r="28" fill="none" stroke="var(--blue)" stroke-width="10" stroke-dasharray="62 176" transform="rotate(-95 35 39)"/><circle cx="35" cy="39" r="28" fill="none" stroke="var(--steel)" stroke-width="10" stroke-dasharray="50 176" transform="rotate(60 35 39)"/><g font-size="3.2" fill="#fff" font-family="Poppins"><text x="14" y="22">30%</text><text x="38" y="70">30%</text></g></svg>
</div>
<div class="t" style="left:419px;top:797px">
  <div class="tm"><i></i>Harrowgate Loadline Works</div>
  <div class="tt">Current Priorities</div>
  <div class="abs" style="left:112px;top:17px;width:1px;height:20px;background:#ccc"></div>
  <div class="tiny" style="left:70px;top:35px">A way to people</div>
  <div class="num" style="left:60px;top:40px;font-size:32px;letter-spacing:-1px">9<span style="color:var(--steel)">.</span>7B</div>
  <div class="tiny" style="left:77px;top:84px;color:#222;font-weight:600">Business Waste</div>
  <div class="abs" style="left:143px;top:21px;width:9px;height:9px;border-radius:50%;background:var(--steel-light)"></div>
  <div class="tiny" style="left:143px;top:36px;writing-mode:vertical-rl;color:#222">Good idea here</div>
</div>
<div class="t" style="left:612px;top:797px">
  <div class="tm"><i></i>Harrowgate Loadline Works</div>
  <div class="tt">Key Insides</div>
  <div class="num" style="left:9px;top:52px;font-size:9px;color:var(--steel)">90B</div>
  <div class="tiny" style="left:9px;top:64px;width:50px">Short paragraph about this insight for the board.</div>
  <div class="abs" style="left:9px;top:80px;width:8px;height:8px;border:.5px solid #999;border-radius:50%"></div>
  <div class="tiny" style="left:20px;top:80px;width:38px"><b style="color:#222">M. Objectives</b><br>Short note</div>
  <div class="abs" style="left:87px;top:10px;width:35px;height:1.5px;background:var(--blue)"></div>
  <div class="abs" style="left:87px;top:45px;width:35px;height:1px;background:#bbb"></div>
  <div class="tiny" style="left:87px;top:16px;width:34px"><b style="color:#222;font-size:3.6px">01</b><br><b style="color:#222">User Growth</b><br>Short note here</div>
  <div class="tiny" style="left:87px;top:52px;width:34px"><b style="color:#222;font-size:3.6px">02</b><br><b style="color:#222">Products</b><br>Short note here</div>
  <div class="tiny" style="left:130px;top:20px;width:34px"><b style="color:#222;font-size:3.6px">03</b><br><b style="color:#222">Revenue</b><br>Short note here</div>
  <div class="tiny" style="left:130px;top:60px;width:34px"><b style="color:#222;font-size:3.6px">04</b><br><b style="color:#222">Seamless</b><br>Short note here</div>
</div>
<div class="t" style="left:805px;top:797px">
  <div class="tm"><i></i>Harrowgate Loadline Works</div>
  <div class="abs" style="left:116px;top:0;width:53px;height:95px;background:#e9ecef"></div>
  <div class="tt">Funding<br>Usage Plan</div>
  <svg class="abs" style="left:9px;top:52px" width="60" height="40"><circle cx="7" cy="7" r="5" fill="none" stroke="#bbb" stroke-width=".6"/><circle cx="7" cy="27" r="5" fill="none" stroke="#bbb" stroke-width=".6"/><path d="M18 2 V34" stroke="#ccc" stroke-width=".5"/></svg>
  <div class="num" style="left:31px;top:55px;font-size:8px">$1.3<small style="font-size:3px">BILLION</small></div>
  <div class="num" style="left:31px;top:75px;font-size:8px">$5.2<small style="font-size:3px">MILLION</small></div>
  <svg class="abs" style="left:77px;top:12px" width="82" height="82" viewBox="0 0 82 82"><circle cx="41" cy="41" r="33" fill="var(--steel)"/><path d="M41 41 L41 6 A35 35 0 0 1 75 53 Z" fill="var(--red)"/><path d="M41 41 L72 55 A33 33 0 0 1 41 74 Z" fill="#dfe6ed"/><circle cx="41" cy="41" r="12" fill="#fff"/><g font-family="Oswald" font-weight="600"><text x="52" y="32" font-size="9" fill="#fff">30%</text><text x="10" y="47" font-size="7" fill="#1e2329">60%</text><text x="47" y="68" font-size="6" fill="#1e2329">10%</text></g></svg>
</div>
<div class="t" style="left:998px;top:797px;background:#0d1114">
  <div class="abs" style="left:4px;top:4px;width:161px;height:87px;background:linear-gradient(120deg,#0f1b26,#1d3c58 55%,#2b5f8a)" role="img" aria-label="Dark blue background with photo area"></div>
  <div class="tm" style="color:#fff;right:7px;top:6px"><i style="border-color:#fff"></i>Harrowgate Loadline Works</div>
  <div class="abs cond" style="left:87px;top:13px;font-size:62px;color:#06090c;line-height:1">10</div>
  <div class="abs cond" style="left:63px;top:35px;font-size:34px;color:#fff;line-height:1;letter-spacing:-1.5px">2049</div>
  <div class="abs" style="left:59px;top:22px;font-size:3px;font-weight:600;color:#fff;line-height:1.2">GOOD IDEA<br>MAKES EVERYTHING<br>IS BETTER IN</div>
</div>

<!-- row 4 -->
<div class="t" style="left:33px;top:916px">
  <div class="tm"><i></i>Harrowgate Loadline Works</div>
  <div class="tt">User Growth</div>
  <div class="num" style="left:9px;top:45px;font-size:10px;color:var(--red)">2.10B</div>
  <div class="tiny" style="left:9px;top:56px">Billion</div>
  <div class="tiny" style="left:9px;top:62px;width:40px;color:#222"><b>Good idea</b> makes everything better</div>
  <div class="num" style="left:9px;top:73px;font-size:10px;color:var(--steel)">1.09M</div>
  <svg class="abs" style="left:55px;top:20px" width="110" height="70"><g stroke="#eee" stroke-width=".4"><path d="M0 8 H108 M0 30 H108 M0 52 H108"/></g><g fill="var(--navy)"><rect x="42" y="42" width="3" height="22"/><rect x="50" y="40" width="3" height="24"/><rect x="58" y="36" width="3" height="28"/><rect x="74" y="30" width="3" height="34"/><rect x="82" y="24" width="3" height="40"/><rect x="90" y="18" width="3" height="46"/><rect x="98" y="6" width="3" height="58"/></g><g fill="var(--steel)"><rect x="34" y="50" width="3" height="14"/><rect x="66" y="34" width="3" height="30"/></g></svg>
</div>
<div class="t" style="left:226px;top:916px">
  <div class="tm"><i></i>Harrowgate Loadline Works</div>
  <div class="tt">ARR</div>
  <svg class="abs" style="left:14px;top:30px" width="56" height="60"><g fill="var(--navy)"><rect x="2" y="2" width="6" height="52"/><rect x="13" y="22" width="6" height="32"/><rect x="24" y="10" width="6" height="44"/><rect x="35" y="36" width="6" height="18"/><rect x="46" y="42" width="5" height="12"/></g></svg>
  <div class="abs" style="left:74px;top:33px;width:40px;height:52px;background:var(--steel)"></div>
  <div class="abs" style="left:121px;top:33px;width:40px;height:52px;background:#8d9399"></div>
  <svg class="abs" style="left:74px;top:33px" width="90" height="30"><path d="M8 22 L16 14 L22 18 L32 8" stroke="#fff" stroke-width=".8" fill="none"/><path d="M56 22 L62 18 L68 8 L76 20" stroke="#fff" stroke-width=".8" fill="none"/></svg>
  <div class="num" style="left:79px;top:63px;font-size:12px;color:#fff">90%</div>
  <div class="num" style="left:126px;top:63px;font-size:12px;color:#fff">10%</div>
</div>
<div class="t" style="left:419px;top:916px">
  <div class="tm"><i></i>Harrowgate Loadline Works</div>
  <div class="tt">MRR</div>
  <div class="tiny" style="left:9px;top:50px;color:#7f9bb5;font-size:3px">What am I Seeing</div>
  <div class="tiny" style="left:9px;top:56px;width:45px">Short paragraph about the monthly revenue result here.</div>
  <div class="num" style="left:9px;top:77px;font-size:10px">2M</div>
  <svg class="abs" style="left:26px;top:76px" width="30" height="12"><path d="M5 2 V10 M1 6 H9" stroke="#ddd" stroke-width="1.5"/><path d="M15 6 L19 10 L27 1" stroke="var(--red)" stroke-width="1.8" fill="none"/></svg>
  <div class="abs" style="left:72px;top:31px;width:88px;height:52px;border:.6px dashed #aaa"></div>
  <div class="abs" style="left:102px;top:55px;width:26px;height:5px;border:.4px solid #bbb;font-size:2.5px;text-align:center;line-height:5px">Insert Picture</div>
</div>
<div class="t" style="left:612px;top:916px">
  <div class="tm"><i></i>Harrowgate Loadline Works</div>
  <div class="tt">Products Matrix</div>
  <div class="abs" style="left:62px;top:30px;width:45px;height:30px;border:.5px solid #ccc"></div>
  <div class="num" style="left:9px;top:43px;font-size:10px">6%</div>
  <div class="num" style="left:71px;top:43px;font-size:10px;color:var(--red)">9%</div>
  <div class="num" style="left:131px;top:43px;font-size:10px">7%</div>
  <div class="num" style="left:9px;top:73px;font-size:10px">32%</div>
  <div class="num" style="left:71px;top:73px;font-size:10px">25%</div>
  <div class="num" style="left:131px;top:73px;font-size:10px">62%</div>
  <div class="tiny" style="left:9px;top:55px;color:#222">Visitor To Trail</div>
  <div class="tiny" style="left:71px;top:55px;color:#222">Free To Paid</div>
  <div class="tiny" style="left:131px;top:55px;color:#222">Activation rate</div>
  <div class="tiny" style="left:9px;top:85px;color:#222">01 Retention</div>
  <div class="tiny" style="left:71px;top:85px;color:#222">W3 Retention</div>
  <div class="tiny" style="left:131px;top:85px;color:#222">Referral rate</div>
</div>
<div class="t" style="left:805px;top:916px">
  <div class="tm"><i></i>Harrowgate Loadline Works</div>
  <div class="tt">Leadership Team</div>
  <div class="tiny" style="left:16px;top:42px;width:28px;text-align:center;color:#222">Good idea makes everything better</div>
  <div class="abs" style="left:80px;top:32px;width:39px;height:54px;border:.6px dashed #aaa"></div>
  <div class="abs" style="left:122px;top:33px;width:22px;height:5px;border-radius:3px;background:var(--blue);font-size:2.5px;color:#fff;text-align:center;line-height:5px">@username</div>
  <div class="abs cond" style="left:122px;top:42px;font-size:5px">Dana Corvell</div>
  <div class="tiny" style="left:122px;top:49px">Post Title</div>
  <div class="abs" style="left:-4px;top:60px;width:8px;height:26px;border:.5px dashed #aaa"></div>
  <div class="abs" style="left:19px;top:60px;width:23px;height:26px;border:.5px dashed #aaa"></div>
  <div class="abs" style="left:49px;top:60px;width:23px;height:26px;border:.5px dashed #aaa"></div>
  <div class="abs" style="left:126px;top:60px;width:23px;height:26px;border:.5px dashed #aaa"></div>
  <div class="abs" style="left:156px;top:60px;width:23px;height:26px;border:.5px dashed #aaa"></div>
</div>
<div class="t" style="left:998px;top:916px">
  <div class="tm"><i></i>Harrowgate Loadline Works</div>
  <div class="tt">Company at Glance</div>
  <div class="num" style="left:9px;top:63px;font-size:10px;color:var(--red)">2.10B</div>
  <div class="tiny" style="left:9px;top:74px">Total Funding</div>
  <div class="tiny" style="left:9px;top:80px;width:40px;color:#222"><b>Good idea</b> makes everything better</div>
  <svg class="abs" style="left:66px;top:22px" width="100" height="70"><g stroke="#eee" stroke-width=".4"><path d="M0 12 H96 M0 26 H96 M0 40 H96 M0 54 H96"/></g><path d="M2 50 L14 44 L24 48 L36 30 L46 38 L56 34 L64 42 L74 28 L84 36 L92 8 L96 14 L96 62 L2 62Z" fill="var(--steel-light)" opacity=".5"/><path d="M2 50 L14 44 L24 48 L36 30 L46 38 L56 34 L64 42 L74 28 L84 36 L92 8 L96 14" stroke="var(--navy)" stroke-width=".8" fill="none"/><path d="M2 54 L20 50 L36 38 L56 44 L74 36 L96 26" stroke="#999" stroke-width=".5" fill="none"/></svg>
</div>

<!-- row 5 -->
<div class="t" style="left:33px;top:1036px">
  <div class="tm"><i></i>Harrowgate Loadline Works</div>
  <div class="tt">Product Roadmap</div>
  <div class="abs" style="left:10px;top:24px;width:145px;height:60px;background:linear-gradient(90deg,#e6edf3,#f8f9fa)"></div>
  <div class="abs" style="left:15px;top:30px;width:50px;height:7px;background:#dfe6ed;border-radius:3px"></div>
  <div class="abs" style="left:85px;top:35px;width:60px;height:7px;background:#dfe6ed;border-radius:3px"></div>
  <div class="abs" style="left:28px;top:46px;width:55px;height:7px;background:var(--blue);border-radius:3px"></div>
  <div class="abs" style="left:98px;top:54px;width:45px;height:7px;background:#fff;border:.4px solid #ccc;border-radius:3px"></div>
  <div class="abs" style="left:58px;top:64px;width:65px;height:7px;background:var(--steel);border-radius:3px"></div>
  <div class="abs" style="left:9px;top:87px;width:152px;display:flex;justify-content:space-between;font-size:2.6px;font-weight:600"><span>Q1 2025</span><span>Q2 2026</span><span>Q3 2027</span><span>Q4 2028</span><span>Q1 2029</span><span>Q2 2030</span><span>Q3 2031</span></div>
</div>
<div class="t" style="left:226px;top:1036px">
  <div class="tm"><i></i>Harrowgate Loadline Works</div>
  <div class="tt">Finances</div>
  <div class="abs" style="left:53px;top:34px;width:56px;height:7px;background:var(--steel)"></div>
  <div class="abs" style="left:53px;top:34px;width:56px;display:flex;font-size:2.6px;color:#fff;line-height:7px"><span style="width:28px;text-align:center">2026</span><span style="width:28px;text-align:center">2027</span></div>
  <svg class="abs" style="left:12px;top:41px" width="100" height="40"><g stroke="#ddd" stroke-width=".4"><path d="M0 5 H97 M0 10 H97 M0 15 H97 M0 20 H97 M0 25 H97 M0 30 H97 M0 35 H97"/></g><rect x="41" y="0" width="28" height="36" fill="var(--steel-light)" opacity=".35"/></svg>
  <div class="tiny" style="left:13px;top:41px;line-height:1.9">Revenue<br>Label · Line item<br>Label · Line item<br>Label · Line item<br>Label · Line item<br>Label · Line item</div>
  <div class="abs" style="left:18px;top:83px;width:4px;height:4px;border-radius:50%;background:var(--steel)"></div>
  <div class="tiny" style="left:25px;top:83px">Short note on these figures</div>
  <div class="num" style="left:118px;top:46px;font-size:11px;color:var(--red)">2.10B</div>
  <div class="tiny" style="left:118px;top:58px">Total Funding</div>
  <div class="tiny" style="left:118px;top:64px;width:45px;color:#222"><b>Good idea</b> makes everything better</div>
</div>
<div class="t" style="left:419px;top:1036px">
  <div class="tm"><i></i>Harrowgate Loadline Works</div>
  <div class="tt">Deep Dives</div>
  <div class="abs" style="left:10px;top:33px;width:70px;height:52px;border:.5px solid #ccc"></div>
  <div class="abs" style="left:89px;top:33px;width:70px;height:52px;border:.5px solid #ccc"></div>
  <div class="abs" style="left:24px;top:35px;width:42px;height:7px;background:var(--blue);font-size:2.6px;color:#fff;text-align:center;line-height:7px">TOPIC ONE</div>
  <div class="abs" style="left:103px;top:35px;width:42px;height:7px;background:var(--slate);font-size:2.6px;color:#fff;text-align:center;line-height:7px">TOPIC TWO</div>
  <div class="tiny" style="left:14px;top:46px;width:62px;text-align:center"><b style="color:#222">STRATEGIC CHALLENGE</b><br>Short note about this first topic</div>
  <div class="num" style="left:36px;top:66px;font-size:9px">90%</div>
  <div class="num" style="left:113px;top:50px;font-size:9px">10%</div>
  <div class="tiny" style="left:93px;top:62px;width:62px;text-align:center"><b style="color:#222">POSSIBLE OBSTACLE</b><br>Short note about this second topic</div>
</div>
<div class="t" style="left:612px;top:1036px">
  <div class="tt" style="left:56px;top:16px">Possible Obstacle</div>
  <div class="abs" style="left:58px;top:44px;width:32px;height:44px;background:var(--navy)"></div>
  <div class="num" style="left:63px;top:50px;font-size:7px;color:#fff">01</div>
  <div class="num" style="left:99px;top:50px;font-size:7px">02</div>
  <div class="num" style="left:135px;top:50px;font-size:7px">03</div>
  <div class="tiny" style="left:63px;top:62px;width:24px;color:#dde"><b style="color:#fff">Converter</b><br>Short note here</div>
  <div class="tiny" style="left:99px;top:62px;width:24px"><b style="color:#222">Converter</b><br>Short note here</div>
  <div class="tiny" style="left:135px;top:62px;width:24px"><b style="color:#222">Converter</b><br>Short note here</div>
</div>
<div class="t" style="left:805px;top:1036px;background:var(--red)">
  <div class="abs cond" style="left:46px;top:26px;font-size:29px;color:#fff;letter-spacing:-1px">Q&amp;A</div>
  <div class="abs cond" style="left:78px;top:15px;font-size:44px;color:#1e1e1e;line-height:1">?</div>
  <div class="abs cond" style="left:102px;top:38px;font-size:5.5px;color:#fff;line-height:1.2;font-weight:500">Question<br>And<br>Answer</div>
</div>
<div class="t" style="left:998px;top:1036px">
  <div class="abs" style="left:6px;top:6px;width:157px;height:83px;background:var(--slate)"></div>
  <div class="abs cond" style="left:30px;top:34px;font-size:21px;color:#fff;font-weight:500">End</div>
  <div class="abs" style="left:82px;top:36px;width:.6px;height:22px;background:#8a939b"></div>
  <div class="abs" style="left:112px;top:28px;width:10px;height:10px;border-radius:50%;border:1px solid #fff"></div>
  <div class="abs" style="left:97px;top:42px;width:40px;text-align:center;font-family:'Oswald',sans-serif;font-weight:500;font-size:4.6px;line-height:1.15;color:#fff;text-transform:uppercase">Harrowgate<br>Loadline Works</div>
</div>

</body>
</html>
```